Design WordPress Website for Contractor App Website

I need a graphic design for a WordPress website for our SaaS called Velturn Software. Please design the landing (Home) page first, before designing other pages. You can design other pages if your landing page is selected.

The design should be modern with a startup feel. The link to the google doc below provides more information. And the attached image has the logo and some screenshots you can use. Copy text from the competitor's site listed as placeholders text or use Lorem Ipsum where needed.

https://files.brindlemark.example/doc/7Qx2Lm9RzT4vKp8NwYc3HsJd5Fg6BtXa/view?mode=read

Target Market(s)

Contractors, painters, plumbers, handymen, electricians, carpenters, landscapers, roofers, home service business.

Industry/Entity Type

Home Improvement

Number of Pages Required

5+ page

Colors
ffc214
34a6d7
9bcb3c

Requirements
Must have
• Look, professionals
Play Store and App Store download icons
Focused on contractors
Nice to have
• Section for video

```html
<!DOCTYPE html>
<html lang="en">
<head>
<meta charset="utf-8">
<title>Velturn – Field Service Management</title>
<link href="https://fonts.googleapis.com/css2?family=Ubuntu:wght@300;400;500;700&family=Montserrat:wght@400;500;600;700&display=swap" rel="stylesheet">
<style>
:root{
  --blue:#73a0cd;
  --blue-deep:#5f8fc2;
  --yellow:#ffc214;
  --navy:#0f1b3d;
  --text:#6b6f7b;
  --muted:#9aa0ad;
  --white:#ffffff;
  --green:#17a14a;
  --cyan:#1fa9dd;
}
*{margin:0;padding:0;box-sizing:border-box}
html,body{width:1200px;height:3032px;overflow:hidden}
body{position:relative;background:var(--white);font-family:"Montserrat",sans-serif;color:var(--text)}
.abs{position:absolute}
.heading{font-family:"Ubuntu",sans-serif;color:var(--navy);font-weight:500}
.light{font-weight:300}
.btn{position:absolute;background:var(--yellow);color:var(--white);font-family:"Montserrat",sans-serif;font-weight:600;display:flex;align-items:center;justify-content:center;letter-spacing:.5px}

/* hero */
.hero-bg{position:absolute;left:0;top:0;width:1200px;height:600px}
.nav-logo{left:125px;top:22px;display:flex;align-items:center;gap:8px;color:var(--white);font-family:"Ubuntu",sans-serif;font-weight:500;font-size:17px;letter-spacing:2px}
.nav-logo .dot{width:24px;height:24px;border-radius:50%;background:var(--white)}
.nav-link{position:absolute;top:27px;font-size:10px;line-height:12px;color:var(--white);letter-spacing:.5px;white-space:nowrap}
.nav-user{left:1115px;top:22px}
.hero-title{left:235px;top:200px;font-size:35px;line-height:41px;color:var(--white)}
.hero-sub{left:235px;top:300px;width:370px;font-size:13px;line-height:15px;color:var(--white)}
.hero-btn{left:234px;top:358px;width:132px;height:33px;font-size:10px;gap:12px}
.hero-version{left:380px;top:370px;font-size:9.5px;color:var(--white)}
.hero-version b{font-weight:700;margin-left:4px}
.phones{left:700px;top:82px;width:440px;height:518px;border-radius:40px;background:linear-gradient(160deg,#2a2d33 0%,#f0f2f5 40%,#fbe3d8 100%)}

/* services */
.service{position:absolute;top:635px;width:220px;text-align:center}
.service svg{display:block;margin:0 auto}
.service h3{font-family:"Ubuntu",sans-serif;font-weight:400;font-size:12.5px;color:var(--navy);margin-top:20px}
.service p{font-size:10px;line-height:17.5px;margin-top:14px;color:var(--text)}
.dots{left:584px;top:827px;display:flex;gap:4px;align-items:center}
.dots span{width:6px;height:6px;border-radius:50%;background:#dcdcdc}
.dots span.on{width:11px;height:11px;background:#c5c5c5}

/* features */
.center{left:0;width:1200px;text-align:center}
.feat-title{top:903px;font-size:31px}
.section-sub{font-size:13px;color:var(--text)}
.tabs{left:350px;top:1008px;display:flex;gap:20px;font-size:11px;color:#6e8fc0}
.tabs span{display:flex;align-items:center;gap:6px;padding:0 5px 12px}
.tabs .active{color:var(--navy);font-weight:500;border-bottom:2px solid var(--yellow)}
.split-title{left:235px;top:1176px;font-size:30px;line-height:37px}
.split-text{left:236px;top:1272px;width:360px;font-size:13px;line-height:19px;color:var(--muted);white-space:nowrap}
.split-btn{left:233px;top:1369px;width:152px;height:32px;font-size:6px}
.photo{left:618px;top:1063px;width:347px;height:453px;background:linear-gradient(160deg,#d8d5d2 0%,#c9b7a6 45%,#b69070 100%);box-shadow:0 10px 30px rgba(0,0,0,.12)}

/* band */
.band{left:0;top:1580px;width:1200px;height:393px;background:var(--blue)}
.band-title{top:1662px;font-size:30px;line-height:36px;color:var(--white)}
.band-text{top:1744px;font-size:13px;line-height:19px;color:var(--white)}
.band-btn{left:496px;top:1812px;width:207px;height:44px;font-size:8.5px}
.band-version{top:1870px;font-size:9.5px;color:var(--white)}

/* testimonials */
.clients-title{top:2022px;font-size:31px;line-height:37px}
.card{position:absolute;top:2172px;width:231px;height:241px;background:var(--white);box-shadow:0 8px 30px rgba(80,100,140,.10);padding:28px 25px}
.stars{color:var(--yellow);font-size:13px;letter-spacing:2px}
.card p{font-size:11.5px;line-height:19px;margin-top:14px;color:var(--text)}
.person{display:flex;align-items:center;gap:12px;margin-top:20px}
.avatar{width:34px;height:34px;border-radius:50%;background:#c9d3e3;position:relative}
.avatar i{position:absolute;left:9px;bottom:-5px;width:14px;height:14px;border-radius:50%;background:#2f6de0}
.person b{display:block;font-family:"Ubuntu",sans-serif;font-weight:500;font-size:16px;color:var(--navy)}
.person small{font-size:8.5px;color:var(--text)}

/* footer */
.footer-bg{left:0;top:2470px;width:1200px;height:562px}
.news-title{left:272px;top:2610px;font-size:30px;color:var(--white)}
.news-sub{left:272px;top:2650px;font-size:12px;color:#dbe6f3}
.news-input{left:749px;top:2620px;width:207px;height:44px;background:#87aed6;color:#e4edf7;font-size:9.5px;padding:17px 20px}
.news-send{left:956px;top:2620px;width:46px;height:44px;background:var(--yellow);display:flex;align-items:center;justify-content:center}
.divider{left:272px;top:2707px;width:730px;height:1px;background:#8db3da}
.foot-logo{left:272px;top:2750px;display:flex;align-items:center;gap:10px;color:var(--white);font-family:"Ubuntu",sans-serif;font-weight:500;font-size:20px;letter-spacing:2.5px}
.foot-logo .dot{width:29px;height:29px;border-radius:50%;background:var(--white)}
.foot-desc{left:272px;top:2803px;width:320px;font-size:10.5px;line-height:19px;color:#e1ebf6}
.foot-h{font-family:"Ubuntu",sans-serif;font-size:15px;color:var(--white)}
.quick{left:650px;top:2800px;font-size:9.5px;color:#e6eef8;line-height:27.7px}
.contact{left:837px;top:2800px;font-size:10px;line-height:17px;color:var(--white)}
.contact span{color:#3a5da8}
.copyright{left:272px;top:2950px;font-size:9.5px;color:#e6eef8}
.legal{left:846px;top:2950px;display:flex;gap:28px;font-size:10px;color:var(--white);font-weight:500}
</style>
</head>
<body>

<!-- Hero -->
<svg class="hero-bg" viewBox="0 0 1200 600" preserveAspectRatio="none" aria-hidden="true">
  <path d="M0 0H1200V420C1100 440 900 470 700 490C500 510 400 520 320 540C170 580 60 460 0 340Z" fill="#73a0cd"/>
</svg>
<div class="abs nav-logo"><span class="dot"></span>VELTURN</div>
<nav>
  <span class="nav-link" style="left:680px">HOME</span>
  <span class="nav-link" style="left:742px">FEATURES</span>
  <span class="nav-link" style="left:824px">PRICING</span>
  <span class="nav-link" style="left:897px">SERVICES</span>
  <span class="nav-link" style="left:977px">BLOG</span>
  <span class="nav-link" style="left:1035px">CONTACT</span>
</nav>
<svg class="abs nav-user" width="20" height="20" viewBox="0 0 20 20" aria-hidden="true"><circle cx="10" cy="10" r="8.5" fill="none" stroke="#fff" stroke-width="1.3"/><circle cx="10" cy="8" r="3" fill="none" stroke="#fff" stroke-width="1.3"/><path d="M4.5 15.5c1.5-2.5 9.5-2.5 11 0" fill="none" stroke="#fff" stroke-width="1.3"/></svg>

<h1 class="abs heading hero-title">Field Service Management<br>has never&nbsp; been <span class="light">Easier</span></h1>
<p class="abs hero-sub">Stay one step ahead of your competition with Change orders, Sales report, Estimate Sections, Web &amp; Social links and more!</p>
<div class="btn hero-btn">DOWNLOAD <svg width="12" height="8" viewBox="0 0 12 8"><path d="M0 4H10M7 1l3 3-3 3" fill="none" stroke="#fff" stroke-width="1.2"/></svg></div>
<div class="abs hero-version">Version 1.04 <b>Whats new?</b></div>
<div class="abs phones" role="img" aria-label="Two smartphones showing the contractor app menu and a new invoice client list"></div>

<!-- Services -->
<div class="service" style="left:240px">
  <svg width="58" height="58" viewBox="0 0 58 58" aria-hidden="true"><rect x="11" y="11" width="36" height="36" rx="6" transform="rotate(45 29 29)" fill="#ffc214" stroke="#ffe08a" stroke-width="3"/><circle cx="29" cy="27" r="4" fill="#fff"/><rect x="27.5" y="28" width="3" height="8" rx="1" fill="#fff"/></svg>
  <h3>Locksmith</h3>
  <p>Lorem ipsum dolor sit amet, consectetur adipiscing elit. Donec quis est suscipit nibh vehicula sollicitudin. Nam aliquam</p>
</div>
<div class="service" style="left:490px">
  <svg width="58" height="58" viewBox="0 0 58 58" aria-hidden="true"><rect x="11" y="11" width="36" height="36" rx="6" transform="rotate(45 29 29)" fill="#17a14a" stroke="#8fd3a7" stroke-width="3"/><rect x="21" y="21" width="16" height="16" rx="1.5" fill="none" stroke="#fff" stroke-width="2"/><path d="M25 21V37" stroke="#fff" stroke-width="2"/></svg>
  <h3>Carpet Cleaning</h3>
  <p>Lorem ipsum dolor sit amet, consectetur adipiscing elit. Donec quis est suscipit nibh vehicula sollicitudin. Nam aliquam</p>
</div>
<div class="service" style="left:739px">
  <svg width="58" height="58" viewBox="0 0 58 58" aria-hidden="true"><rect x="11" y="11" width="36" height="36" rx="6" transform="rotate(45 29 29)" fill="#1fa9dd" stroke="#9bd8ef" stroke-width="3"/><path d="M22 23H36M26 23V21H32V23M23.5 23.5L24.5 37H33.5L34.5 23.5M27 26V34M29 26V34M31 26V34" fill="none" stroke="#fff" stroke-width="1.6"/></svg>
  <h3>Junk Removal</h3>
  <p>Lorem ipsum dolor sit amet, consectetur adipiscing elit. Donec quis est suscipit nibh vehicula sollicitudin. Nam aliquam</p>
</div>
<div class="abs dots"><span></span><span class="on"></span><span></span></div>

<!-- Features -->
<h2 class="abs center heading feat-title">Powerful features built <span class="light">for contractors.</span></h2>
<p class="abs center section-sub" style="top:955px">Lorem ipsum dolor sit amet, consectetur adipiscing elit. Donec quis est suscipit nibh vehicula</p>
<div class="abs tabs">
  <span class="active"><svg width="14" height="10" viewBox="0 0 14 10"><rect x="1" y="2" width="12" height="6" rx="3" fill="none" stroke="#0f1b3d" stroke-width="1.3"/></svg>Schedule Jobs</span>
  <span><svg width="12" height="12" viewBox="0 0 12 12"><path d="M1 1H11V8H5L2 11V8H1Z" fill="none" stroke="#6e8fc0" stroke-width="1.1"/><path d="M3 4H9M3 6H7" stroke="#6e8fc0"/></svg>Talk with customer</span>
  <span><svg width="13" height="13" viewBox="0 0 13 13"><path d="M1 1L12 12M12 1L1 12" stroke="#6e8fc0" stroke-width="1.3"/></svg>Do the work</span>
  <span><svg width="13" height="11" viewBox="0 0 13 11"><rect x="1" y="1" width="11" height="9" rx="1" fill="none" stroke="#6e8fc0" stroke-width="1.1"/><path d="M1 4H12" stroke="#6e8fc0"/></svg>Invoice and get paid</span>
</div>
<h2 class="abs heading split-title">Use our app and<br><span class="light">Easily Schedule jobs</span></h2>
<p class="abs split-text">Lorem ipsum dolor sit amet, consectetur adipiscing<br>elit. Donec quis est suscipit nibh vehicula<br>sollicitudin. Nam aliquam ex lacinia nisl<br>consectetur imperdiet.</p>
<div class="btn split-btn">START SCHEDULE RIGHT NOW</div>
<div class="abs photo" role="img" aria-label="Photo of a smiling woman using her phone at a laptop, with review bubbles floating beside her"></div>

<!-- Download band -->
<section class="abs band"></section>
<h2 class="abs center heading band-title" style="color:#fff">Grow your service Business<br><span class="light">with Velturn</span></h2>
<p class="abs center band-text">Lorem ipsum dolor sit amet, consectetur adipiscing elit. Donec quis<br>est suscipit nibh vehicula sollicitudin. Nam aliquam ex lacinia nisl</p>
<div class="btn band-btn">DOWNLOAD OUR APP</div>
<p class="abs center band-version">Version 1.04 &nbsp;<b>Whats new?</b></p>

<!-- Testimonials -->
<h2 class="abs center heading clients-title">Clients Report a 37% Revenue Increase With<br><span class="light">Velturn Service Management Software</span></h2>
<p class="abs center section-sub" style="top:2112px">Lorem ipsum dolor sit amet, consectetur adipiscing elit. Donec quis est suscipit nibh vehicula</p>
<svg class="abs" style="left:156px;top:2284px" width="40" height="12" viewBox="0 0 40 12" aria-hidden="true"><path d="M39 6H2M7 1L2 6l5 5" fill="none" stroke="#9bb7d8" stroke-width="1.2"/></svg>
<svg class="abs" style="left:1004px;top:2284px" width="40" height="12" viewBox="0 0 40 12" aria-hidden="true"><path d="M1 6H38M33 1l5 5-5 5" fill="none" stroke="#9bb7d8" stroke-width="1.2"/></svg>

<article class="card" style="left:234px"><div class="stars">★★★★★</div><p>Monotonectally grow frontend processes and you vision for a Monoto ctally make a&nbsp; disinter mediate client cente with&nbsp; life competitive e-markets.</p><div class="person"><div class="avatar"><i></i></div><div><b>Rowan Ellery</b><small>Ui designer at company name</small></div></div></article>
<article class="card" style="left:484px"><div class="stars">★★★★★</div><p>Monotonectally grow frontend processes and you vision for a Monoto ctally make a&nbsp; disinter mediate client cente with&nbsp; life competitive e-markets.</p><div class="person"><div class="avatar"><i></i></div><div><b>Tessa Marlow</b><small>Ui designer at company name</small></div></div></article>
<article class="card" style="left:734px"><div class="stars">★★★★★</div><p>Monotonectally grow frontend processes and you vision for a Monoto ctally make a&nbsp; disinter mediate client cente with&nbsp; life competitive e-markets.</p><div class="person"><div class="avatar"><i></i></div><div><b>Rowan Ellery</b><small>Ui designer at company name</small></div></div></article>

<!-- Footer -->
<svg class="abs footer-bg" viewBox="0 0 1200 562" preserveAspectRatio="none" aria-hidden="true">
  <path d="M0 220C80 90 220 20 350 8C560 -10 900 70 1200 150V562H0Z" fill="#73a0cd"/>
</svg>
<h2 class="abs heading news-title" style="color:#fff">Subscribe Our&nbsp; Newsletter</h2>
<p class="abs news-sub">Subscribe &amp; get regular news &amp; promotion update.</p>
<div class="abs news-input">Enter&nbsp; email address...</div>
<div class="abs news-send"><svg width="26" height="24" viewBox="0 0 26 24" aria-hidden="true"><path d="M2 11L24 2L18 22L12 14Z M12 14L24 2" fill="none" stroke="#fff" stroke-width="1.8" stroke-linejoin="round"/></svg></div>
<div class="abs divider"></div>
<div class="abs foot-logo"><span class="dot"></span>VELTURN</div>
<p class="abs foot-desc">Uniquely maximize cross-unit sources vis-a-vis corporate portals. Compellingly coordinate pandemic.</p>
<div class="abs foot-h" style="left:646px;top:2764px">Quick Link</div>
<div class="abs quick">Home<br>Features<br>Pricing<br>Services<br>Blog<br>Contact</div>
<div class="abs foot-h" style="left:837px;top:2764px">Contact Info</div>
<div class="abs contact">Mail- <span>hello@velturn.example</span><br><br style="line-height:10px">Location- <span>18 Larkfield Road,<br>Brookvale NY 1205.</span></div>
<p class="abs copyright">Copyright © Velturn2021 - All rights reserved.</p>
<div class="abs legal"><span>Trems &amp; Condition</span><span>Privecy</span></div>

</body>
</html>
```